Flyer to acquire new customers for a craft business

Create an A5 (4 pages in total) flyer describing proposed services from a craft business to new customers.

Services are :

All types of renovation (painting, plastering, attaching wallpapers ....)
All types of repairs
Electric repairs
Little to medium woodworks
Services around the house and garden

Flyer must be translatable into several languages beginning with FRENCH.
Texts are being written by ourselves.

Target Market(s)

Private customers

Industry/Entity Type

Mixed craft business

Colors

Designer to choose colors to be used in the design.

```html
<!DOCTYPE html>
<html lang="fr">
<head>
<meta charset="utf-8">
<title>Atelier Bramel – dépliant A5</title>
<link href="https://fonts.googleapis.com/css2?family=Open+Sans:wght@300;400;600;700&family=Roboto:wght@400;500;700&display=swap" rel="stylesheet">
<style>
  :root{
    --navy:#2a1f4b;
    --navy-deep:#221a3e;
    --navy-soft:#3a2d63;
    --orange:#f2a93b;
    --peach:#fcefe2;
    --ink:#222;
    --grey:#555;
    --paper:#ffffff;
    --stage:#f2f2f2;
  }
  *{box-sizing:border-box;margin:0;padding:0}
  html,body{width:720px;height:1200px;overflow:hidden;background:var(--stage)}
  body{position:relative;font-family:"Roboto",sans-serif;color:var(--ink)}
  .spread{position:absolute;left:20px;width:680px;height:484px;display:flex;box-shadow:0 1px 3px rgba(0,0,0,.12)}
  .spread--outside{top:50px}
  .spread--inside{top:620px}
  .page{position:relative;width:340px;height:484px;overflow:hidden;background:var(--paper)}
  .fold{position:absolute;left:360px;width:0;border-left:1px dashed #7fb6dd}
  .fold--outside{top:20px;height:544px}
  .fold--inside{top:590px;height:544px}

  /* back cover */
  .hero-band{height:70px;background:var(--navy);color:#fff;display:flex;flex-direction:column;justify-content:center;padding-left:54px;font-family:"Open Sans",sans-serif;font-weight:300;font-size:18px;line-height:20px;letter-spacing:.3px}
  .hero-band strong{color:var(--orange);font-weight:700}
  .intro{text-align:center;font-family:"Open Sans",sans-serif;font-size:10.5px;line-height:13px;margin-top:17px;color:var(--ink)}
  .intro em{display:block}
  .cta{text-align:center;font-weight:700;font-size:13.5px;margin-top:15px;color:var(--ink)}
  .photo{display:block}
  .photo--workshop{position:absolute;top:158px;left:0;width:340px;height:205px;background:linear-gradient(135deg,#9c7357 0%,#c79a78 40%,#8b6146 75%,#b48866 100%)}
  .brand-stack{position:absolute;top:372px;left:0;width:340px;text-align:center}
  .brand-dot{display:block;width:30px;height:30px;border-radius:50%;background:var(--navy);margin:0 auto 5px}
  .brand-stack span{font-weight:700;font-size:10.5px;color:var(--navy)}
  .contact{position:absolute;top:414px;font-family:"Open Sans",sans-serif;font-size:7.5px;line-height:10.5px;color:var(--grey)}
  .contact--address{left:50px}
  .contact--reach{left:215px}
  .contact svg{vertical-align:-1px;margin-right:2px}
  .hours{position:absolute;top:456px;font-family:"Open Sans",sans-serif;font-size:5.5px;color:var(--grey)}
  .hours--week{left:58px}
  .hours--sat{left:215px}
  .web-rule{position:absolute;bottom:16px;left:0;width:100%;display:flex;align-items:center;gap:6px;font-family:"Open Sans",sans-serif;font-size:7px;color:var(--navy)}
  .web-rule::before,.web-rule::after{content:"";flex:1;height:1px;background:var(--navy)}
  .web-rule::before{margin-left:0}
  .web-rule--light{color:#fff}
  .web-rule--light::before,.web-rule--light::after{background:#fff}

  /* front cover */
  .masthead{height:135px;display:flex;align-items:center;justify-content:center;gap:10px}
  .masthead-mark{width:14px;height:14px;border-radius:50%;background:var(--navy)}
  .masthead-name{font-weight:700;font-size:20px;color:var(--navy);letter-spacing:.5px}
  .claim-band{height:76px;background:var(--navy);padding:5px 8px 5px 5px}
  .claim-box{height:100%;border:1.5px solid #fff;display:flex;align-items:center;justify-content:center;text-align:center;color:var(--orange);font-weight:700;font-size:16.5px;line-height:22px;letter-spacing:.3px}
  .gallery{position:absolute;top:218px;left:5px;width:320px}
  .gallery-row{display:flex;gap:4px;margin-bottom:5px}
  .photo--grinder{width:160px;height:95px;background:linear-gradient(135deg,#2b2f33 0%,#5b4a36 55%,#c98a3a 100%)}
  .photo--spanners{width:156px;height:95px;background:linear-gradient(135deg,#3a3c40,#8c8f94 60%,#4a4c50)}
  .photo--toolwall{width:320px;height:110px;background:linear-gradient(120deg,#1f3556 0%,#2e5b8f 45%,#1c2e4a 100%)}
  .foot-band{position:absolute;left:0;bottom:0;width:100%;height:29px;background:var(--navy)}
  .foot-band .web-rule{bottom:14px}

  /* inside left */
  .page--about{background:linear-gradient(170deg,var(--navy-soft) 0%,var(--navy) 45%,var(--navy-deep) 100%);color:#fff}
  .about-wave{position:absolute;left:0;top:140px;width:340px;height:344px}
  .about-copy{position:relative;padding:22px 24px 0 29px;font-size:7.7px;line-height:12.5px}
  .about-copy .brand-ref{color:var(--orange)}
  .about-copy p{margin-bottom:3px}
  .about-copy .gap{margin-top:14px}
  .about-list{list-style:none;margin:3px 0 3px}
  .about-list li{padding-left:11px;position:relative}
  .about-list li::before{content:"";position:absolute;left:1px;top:4px;width:6px;height:6px;background:var(--orange);border-radius:1.5px}
  .services{position:relative;margin-top:14px;text-align:center}
  .service{margin-bottom:16px}
  .service svg{display:block;margin:0 auto 5px}
  .service h3{font-size:8.7px;font-weight:700;letter-spacing:.3px}

  /* inside right */
  .crafts-title{text-align:center;margin-top:33px;font-weight:700;font-size:16px;color:var(--navy);text-decoration:underline;text-decoration-thickness:1.5px;text-underline-offset:3px;letter-spacing:.3px}
  .craft{position:absolute;width:340px}
  .craft-frame{position:absolute;width:105px;height:120px;background:var(--peach)}
  .craft-photo{position:absolute;width:120px;height:95px;border-radius:4px;box-shadow:0 2px 4px rgba(0,0,0,.35)}
  .photo--painting{background:linear-gradient(135deg,#6b4a2c,#b9874f 50%,#e5d8c4)}
  .photo--pliers{background:linear-gradient(135deg,#1d1f22,#5e6064 50%,#c48d6d)}
  .photo--wires{background:linear-gradient(135deg,#d9dadc,#3f8ecf 45%,#e0b732 75%,#c8483b)}
  .craft-text{position:absolute;width:145px;font-size:7px;line-height:8.5px;color:var(--grey)}
  .craft-text p{margin-bottom:2.5px;text-align:justify}
  .craft-text--left p{text-align:left}
  .craft-text h3{color:var(--orange);font-weight:700;font-size:13.5px;line-height:13px;margin-bottom:7px;letter-spacing:.3px}
</style>
</head>
<body>

<div class="fold fold--outside"></div>
<div class="fold fold--inside"></div>

<!-- Outside: back cover + front cover -->
<section class="spread spread--outside">
  <article class="page page--back">
    <header class="hero-band">
      <span>VOUS ÊTES À LA RECHERCHE</span>
      <span>D’UN PARTENAIRE <strong>FIABLE</strong></span>
    </header>
    <p class="intro">Pour tous types de travaux et de services de l’artisanat<br>petit, moyens et aussi <strong>plus grands</strong><em>Intervention rapide</em></p>
    <h2 class="cta">Contactez-nous pour un conseil personnalisé</h2>
    <div class="photo photo--workshop" role="img" aria-label="Photo d’un atelier de menuiserie avec des planches de bois empilées"></div>
    <div class="brand-stack">
      <i class="brand-dot"></i>
      <span>Atelier Bramel</span>
    </div>
    <address class="contact contact--address" style="font-style:normal">
      <svg width="7" height="8" viewBox="0 0 10 12"><path d="M5 0a4 4 0 0 0-4 4c0 3 4 8 4 8s4-5 4-8a4 4 0 0 0-4-4z" fill="#f2a93b"/><circle cx="5" cy="4" r="1.5" fill="#fff"/></svg>12, rue des Artisans<br>&nbsp;&nbsp;&nbsp;4410 Belvaux
    </address>
    <address class="contact contact--reach" style="font-style:normal">
      <svg width="7" height="7" viewBox="0 0 10 10"><path d="M2 1l2 2-1 1.5a6 6 0 0 0 2.5 2.5L7 6l2 2-1.5 1.5C4 9 1 6 .5 2.5z" fill="#f2a93b"/></svg>21 40 55 08<br>
      <svg width="7" height="7" viewBox="0 0 10 10"><circle cx="5" cy="5" r="4.5" fill="#f2a93b"/></svg>www.atelierbramel.lu<br>
      <svg width="7" height="6" viewBox="0 0 10 8"><rect x=".5" y=".5" width="9" height="7" fill="none" stroke="#f2a93b"/><path d="M.5 .5L5 4.5 9.5.5" fill="none" stroke="#f2a93b"/></svg>contact@atelierbramel.lu
    </address>
    <p class="hours hours--week">Monday – Friday 9 am to 7 pm</p>
    <p class="hours hours--sat">Saturday 8 am to 1 pm</p>
    <p class="web-rule">www.atelierbramel.lu</p>
  </article>

  <article class="page page--front">
    <div class="masthead">
      <i class="masthead-mark"></i>
      <span class="masthead-name">Atelier Bramel</span>
    </div>
    <div class="claim-band">
      <h1 class="claim-box">Nous réalisons tous vos travaux<br>intérieurs et extérieurs</h1>
    </div>
    <div class="gallery">
      <div class="gallery-row">
        <div class="photo photo--grinder" role="img" aria-label="Photo d’une meuleuse projetant des étincelles"></div>
        <div class="photo photo--spanners" role="img" aria-label="Photo de clés plates dans une caisse à outils"></div>
      </div>
      <div class="photo photo--toolwall" role="img" aria-label="Photo d’un panneau d’outils suspendus avec une main gantée"></div>
    </div>
    <footer class="foot-band"><p class="web-rule web-rule--light">www.atelierbramel.lu</p></footer>
  </article>
</section>

<!-- Inside spread -->
<section class="spread spread--inside">
  <article class="page page--about">
    <svg class="about-wave" viewBox="0 0 340 344" preserveAspectRatio="none" aria-hidden="true">
      <path d="M0 20 C90 -10 200 40 340 10 L340 344 L0 344Z" fill="#ffffff" opacity=".04"/>
      <path d="M0 120 C120 60 230 170 340 110 L340 344 L0 344Z" fill="#000000" opacity=".08"/>
    </svg>
    <div class="about-copy">
      <p><span class="brand-ref">«Atelier Bramel»</span> est une société jeune et dynamique, actif dans le secteur de l’artisanat. Nous proposons des services en général dans le domaine de la construction et de l’habitat.</p>
      <ul class="about-list">
        <li>Une réparation ?</li>
        <li>Une modification ?</li>
        <li>Besoin de support technique ou d’un coup de main ?</li>
      </ul>
      <p>Un simple coup de fil suffit pour une prise en charge professionnelle.</p>
      <p class="gap">«Atelier Bramel» vous propose ses services, que ce soit pour votre habitat, les alentours ou votre société. Flexible et rapide.</p>
    </div>
    <div class="services">
      <div class="service">
        <svg width="38" height="42" viewBox="0 0 38 42"><path d="M19 1L37 11V31L19 41L1 31V11Z" fill="#fff" stroke="#f2a93b" stroke-width="2"/><path d="M11 29l9-9M14 12a4 4 0 0 0 5 5l8 8-2 2-8-8a4 4 0 0 1-5-5l2 2 2-1 1-2z" fill="none" stroke="#f2a93b" stroke-width="1.6" stroke-linejoin="round"/><path d="M27 12l-9 9" stroke="#2a1f4b" stroke-width="1.6"/></svg>
        <h3>Réparations de tout genre</h3>
      </div>
      <div class="service">
        <svg width="38" height="42" viewBox="0 0 38 42"><path d="M19 1L37 11V31L19 41L1 31V11Z" fill="#fff" stroke="#f2a93b" stroke-width="2"/><rect x="10" y="12" width="11" height="10" fill="none" stroke="#2a1f4b" stroke-width="1.4"/><rect x="16" y="19" width="12" height="11" fill="none" stroke="#2a1f4b" stroke-width="1.4"/><path d="M12 17l2 2 5-5M19 25l2 2 5-5" fill="none" stroke="#f2a93b" stroke-width="1.6"/></svg>
        <h3>Services professionnels</h3>
      </div>
      <div class="service">
        <svg width="38" height="42" viewBox="0 0 38 42"><path d="M19 1L37 11V31L19 41L1 31V11Z" fill="#fff" stroke="#f2a93b" stroke-width="2"/><rect x="18" y="11" width="12" height="8" rx="2" fill="none" stroke="#f2a93b" stroke-width="1.4"/><circle cx="21" cy="15" r=".9" fill="#f2a93b"/><circle cx="24" cy="15" r=".9" fill="#f2a93b"/><circle cx="27" cy="15" r=".9" fill="#f2a93b"/><path d="M11 17l3 3-1.5 2a9 9 0 0 0 4 4l2-1.5 3 3-2 2c-5 0-10-5-10.5-10.5z" fill="none" stroke="#2a1f4b" stroke-width="1.4" stroke-linejoin="round"/></svg>
        <h3>Support dans les meilleurs délais</h3>
      </div>
    </div>
  </article>

  <article class="page page--crafts">
    <h2 class="crafts-title">ÄREN HANDWRIERKER</h2>

    <div class="craft" style="top:83px">
      <div class="craft-frame" style="left:17px;top:0"></div>
      <div class="craft-photo photo--painting" style="left:27px;top:10px" role="img" aria-label="Photo de matériel de peinture : rouleaux, pinceaux et ruban"></div>
      <div class="craft-text" style="left:175px;top:10px">
        <h3>Rénovations</h3>
        <p>Nous proposons tous types de rénovations (petite, moyenne ou grande envergure).</p>
        <p>peinture, carrelage, plâtrage, murs en placo-plâtre, sanitaire.</p>
        <p>Nous utilisons des produits standars bien connus mais de même des produits naturels comme l’argile et bien d’autre.</p>
      </div>
    </div>

    <div class="craft" style="top:206px">
      <div class="craft-frame" style="left:187px;top:0"></div>
      <div class="craft-photo photo--pliers" style="left:175px;top:0" role="img" aria-label="Photo d’une main tenant une pince au-dessus d’outils"></div>
      <div class="craft-text craft-text--left" style="left:17px;top:6px;width:150px">
        <h3>Réparations</h3>
        <p>Une fuite d’eau? un remplacement d’un tuyau ou même une extension sanitaire?</p>
        <p>Remplacer du carrelage déffectueux même des petits travaux ?</p>
        <p>Une réparation d’un garde-corps ?</p>
        <p>Le remplacement d’une porte intérieure ?</p>
        <p>Presque tout est possible</p>
      </div>
    </div>

    <div class="craft" style="top:335px">
      <div class="craft-frame" style="left:17px;top:0"></div>
      <div class="craft-photo photo--wires" style="left:27px;top:10px" role="img" aria-label="Photo de matériel électrique : câbles, multimètre et ruban isolant"></div>
      <div class="craft-text" style="left:175px;top:10px">
        <h3>Travaux en<br>électricité</h3>
        <p>Installation de lampadaires, remplacement et extensions de circuits électriques, dépannages en électricité, systèmes d’alarme et de vidéosurveillance ne sont quelques exemples de notre savoir faire.</p>
      </div>
    </div>
  </article>
</section>

</body>
</html>
```